Geschäftspapier für Pfandhaus und Juwelier gesucht
Zielgruppe
Pfandhaus und Juwelier.
Aufgabenstellung
Ich betreibe mehrere Filialen und möchte all diese wir einem Briefkopf haben und ggf Platz für weitere da ich gerade 2 weitere eröffne. Unter www.leihhaus-Borlen.de sieht man Logo und Farben.
Ich möchte das Briefpapier als Datei haben und nicht gedruckt sondern will es selbst am Firmendrucker drucken.Die Bankverbindung sollte auch darauf sein aber erstmal etwas am Platzhalter eintragen .

```html
<!DOCTYPE html>
<html lang="de">
<head>
<meta charset="utf-8">
<title>Leihhaus Borlen – Briefpapier</title>
<link rel="stylesheet" href="https://fonts.googleapis.com/css2?family=Open+Sans:wght@400;700&display=swap">
<style>
  :root{
    --gold:#b09a5e;
    --dark:#4a4a4a;
    --paper:#ffffff;
    --ground:#ececec;
    --ink:#1d1d1d;
    --light:#ffffff;
  }
  *{box-sizing:border-box;margin:0;padding:0}
  html,body{width:1200px;height:1010px;overflow:hidden;background:var(--ground)}
  body{font-family:"Open Sans",Arial,sans-serif;color:var(--ink)}
  .page{position:absolute;left:267px;top:35px;width:665px;height:940px;background:var(--paper);
        box-shadow:0 4px 18px rgba(0,0,0,.12)}
  .top-rule{position:absolute;left:0;top:14px;width:420px;height:3px;background:var(--gold)}
  .brand-block{position:absolute;left:418px;top:8px;width:247px;height:94px;background:var(--dark);
               display:flex;align-items:center;justify-content:center}
  .brand-name{color:var(--gold);font-weight:400;font-size:19px;letter-spacing:.5px;line-height:1.2;text-align:center}
  .brand-name small{display:block;font-size:13px;letter-spacing:2px}
  .branches{position:absolute;left:500px;top:102px;width:158px;height:370px;background:var(--gold);
            color:var(--light);padding:14px 12px 0 14px;font-size:7.6px;line-height:1.38}
  .branches h2{font-size:8px;font-weight:700;letter-spacing:.2px;margin-bottom:7px}
  .branch{margin-bottom:12px}
  .branch .row{display:flex;align-items:center;gap:4px}
  .branch svg{width:7px;height:7px;flex:none}
  .return-line{position:absolute;left:75px;top:162px;font-size:6.6px;text-decoration:underline}
  .recipient{position:absolute;left:75px;top:182px;font-size:10.5px;line-height:1.3;font-style:normal}
  .fold-mark{position:absolute;left:0;width:16px;height:1px;background:#c8c8c8}
  .fold-mark.first{top:282px}
  .fold-mark.second{top:612px}
  .footer{position:absolute;left:0;top:852px;width:665px;height:70px}
  .footer svg{position:absolute;left:0;top:0}
  .bank{position:absolute;left:0;top:22px;display:flex;color:var(--light);font-size:8.4px;line-height:1.3}
  .bank .cell{padding:0 14px;border-left:1px solid rgba(255,255,255,.85)}
  .bank .cell:first-child{border-left:none;padding-left:22px}
  .website{position:absolute;left:470px;top:30px;width:124px;text-align:center;color:var(--light);font-size:9.4px}
</style>
</head>
<body>
<div class="page">
  <div class="top-rule"></div>
  <div class="brand-block">
    <div class="brand-name">Markus Borlen<small>Leihhaus</small></div>
  </div>

  <aside class="branches">
    <h2>MARKUS BORLEN LEIHHAUS</h2>
    <div class="branch">
      <div>Lindenallee 4</div><div>12345 Musterstadt</div>
      <div class="row"><svg viewBox="0 0 10 10"><path d="M2 1h2l1 2.5-1.3 1a6 6 0 0 0 2.8 2.8l1-1.3L10 7v2a1 1 0 0 1-1 1A8 8 0 0 1 1 2a1 1 0 0 1 1-1z" fill="#fff"/></svg>+49 (0) 123 1234500-0</div>
      <div class="row"><svg viewBox="0 0 10 10"><rect x="1" y="3" width="8" height="6" fill="#fff"/><rect x="3" y="1" width="4" height="3" fill="#fff"/></svg>+49 (0) 123 1234500-9</div>
      <div class="row"><svg viewBox="0 0 10 10"><rect x="0.5" y="2" width="9" height="6" fill="#fff"/><path d="M.5 2l4.5 3.5L9.5 2" stroke="#b09a5e" fill="none"/></svg>ms@leihhaus-borlen.de</div>
    </div>
    <div class="branch">
      <div>Gartenstraße 7</div><div>23456 Beispielheim</div>
      <div class="row"><svg viewBox="0 0 10 10"><path d="M2 1h2l1 2.5-1.3 1a6 6 0 0 0 2.8 2.8l1-1.3L10 7v2a1 1 0 0 1-1 1A8 8 0 0 1 1 2a1 1 0 0 1 1-1z" fill="#fff"/></svg>+49 (0) 234 5550123-5</div>
      <div class="row"><svg viewBox="0 0 10 10"><rect x="1" y="3" width="8" height="6" fill="#fff"/><rect x="3" y="1" width="4" height="3" fill="#fff"/></svg>+49 (0) 234 5550123-0</div>
      <div class="row"><svg viewBox="0 0 10 10"><rect x="0.5" y="2" width="9" height="6" fill="#fff"/><path d="M.5 2l4.5 3.5L9.5 2" stroke="#b09a5e" fill="none"/></svg>bh@leihhaus-borlen.de</div>
    </div>
    <div class="branch">
      <div>Am Markt 21</div><div>34567 Altdorf</div>
      <div class="row"><svg viewBox="0 0 10 10"><path d="M2 1h2l1 2.5-1.3 1a6 6 0 0 0 2.8 2.8l1-1.3L10 7v2a1 1 0 0 1-1 1A8 8 0 0 1 1 2a1 1 0 0 1 1-1z" fill="#fff"/></svg>+49 (0) 3456 5550400</div>
      <div class="row"><svg viewBox="0 0 10 10"><rect x="1" y="3" width="8" height="6" fill="#fff"/><rect x="3" y="1" width="4" height="3" fill="#fff"/></svg>+49 (0) 3456 5550408</div>
      <div class="row"><svg viewBox="0 0 10 10"><rect x="0.5" y="2" width="9" height="6" fill="#fff"/><path d="M.5 2l4.5 3.5L9.5 2" stroke="#b09a5e" fill="none"/></svg>ad@leihhaus-borlen.de</div>
    </div>
    <div class="branch">
      <div>Kirchgasse 15</div><div>45678 Neuhausen</div>
      <div class="row"><svg viewBox="0 0 10 10"><path d="M2 1h2l1 2.5-1.3 1a6 6 0 0 0 2.8 2.8l1-1.3L10 7v2a1 1 0 0 1-1 1A8 8 0 0 1 1 2a1 1 0 0 1 1-1z" fill="#fff"/></svg>+49 (0) 456 55503217</div>
      <div class="row"><svg viewBox="0 0 10 10"><rect x="1" y="3" width="8" height="6" fill="#fff"/><rect x="3" y="1" width="4" height="3" fill="#fff"/></svg>+49 (0) 456 55503219</div>
      <div class="row"><svg viewBox="0 0 10 10"><rect x="0.5" y="2" width="9" height="6" fill="#fff"/><path d="M.5 2l4.5 3.5L9.5 2" stroke="#b09a5e" fill="none"/></svg>nh@leihhaus-borlen.de</div>
    </div>
    <div class="branch">
      <div>Schillerweg 3</div><div>56789 Bergfelden</div>
      <div class="row"><svg viewBox="0 0 10 10"><path d="M2 1h2l1 2.5-1.3 1a6 6 0 0 0 2.8 2.8l1-1.3L10 7v2a1 1 0 0 1-1 1A8 8 0 0 1 1 2a1 1 0 0 1 1-1z" fill="#fff"/></svg>+49 (0) 567 55512</div>
      <div class="row"><svg viewBox="0 0 10 10"><rect x="0.5" y="2" width="9" height="6" fill="#fff"/><path d="M.5 2l4.5 3.5L9.5 2" stroke="#b09a5e" fill="none"/></svg>bf@leihhaus-borlen.de</div>
    </div>
  </aside>

  <p class="return-line">Markus Borlen Leihhaus | Lindenallee 4 | 12345 Musterstadt</p>
  <address class="recipient">
    Herr<br>Mark Mustermann<br>Musterweg 13<br>24102 Dortmund
  </address>

  <div class="fold-mark first"></div>
  <div class="fold-mark second"></div>

  <footer class="footer">
    <svg width="665" height="70" viewBox="0 0 665 70">
      <polygon points="0,18 462,18 452,64 0,64" fill="var(--gold)"/>
      <polygon points="472,6 604,6 592,64 460,64" fill="var(--dark)"/>
      <polygon points="614,18 665,18 665,64 602,64" fill="var(--gold)"/>
    </svg>
    <div class="bank">
      <div class="cell">Bankverbindung:<br>Markus Borlen</div>
      <div class="cell">Musterbank<br>USt-ID-Nr. DEXXXXXXXXX</div>
      <div class="cell">IBAN: DEXX XXXX XXXX XXXX XXXX X<br>BIC: XXXXXXXX</div>
    </div>
    <div class="website">www.leihhaus-borlen.de</div>
  </footer>
</div>
</body>
</html>
```